New Design for Accounting Firm

CLIENT NAME: Corvanta
CURRENT WEBSITE: www.corvantagroup.example.com.au

CLIENTS THE CLIENT LIKES:
http://velduro.example.se/
http://www.layerport.example.biz/index.php
http://www.plinthworks.example.co.uk/
http://www.worldreliefmonitor.example.org/

COLOUR THEMES:
Colour theme to reflect the logo, with a leaning to blue in Accounting & Audit sections and green in Super section.

LOOK AND FEEL:
The look and feel needs to reflect an accessible culture and contemporary sensibility while still communicating our experience and stability as a professional company.

ABOUT:
The concept of 'Corvanta' is integral to our identity. Definition: 'The connection of creative ideas from a group of diverse individuals, applied with the end aim of solving practical problems'. See ''About Us'' on our website for more.

OTHER DETAILS:
Our three divisions (and service areas within each division) must be easily navigated as they related to very different users of the site. Two client sign in sections (Accounting & Super) must be easily distinguished to avoid user confusion.

MENU STRUCTURE:
* About
- includes history, values, our people, community etc
* Accounting & Advisory
- About
- Services
- Tax & Accounting
- Business Advisory
- Family Wealth Management
- Client Sign In
- Calculators
* Audit & Assurance
- About
- Services
* Corvanta Super
- About
- Individuals
- Services
- Advisers
- Services
- Portal Sign In
- Calculators
* Careers
* Newsletters
* Contact

REQUIREMENTS:
- Layered PSD form home and content pages
- No coding required, we use our own CMS to insert XHTML files into.
Updates

Hi Guys,

The client has asked for a non-cliche'd images in the design. If you'd like to try again with some images that represent the business but aren't your standard boring accounting-looking people, then please do! Cliche is a killer in design - please pump some creativity in!

Cheers,
Ned.

Reason: GUYS - PLEASE LISTEN TO THESE COMMENTS - I'VE SAID THEM TWICE NOW AND PEOPLE ARE STILL POSTING PROJECTS WITH CLICHED AND OBVIOUS ACCOUTNING TYPE IMAGES. USE YOUR CREATIVITY AND POST A DESIGN THAT IS OUTSIDE THE BOX WITH REGARDS TO THE IMAGES YOU ARE USING.

Reason: I am waiting to hear back from the client on their decision.

Industry/Entity Type

Accounting

```html
<!DOCTYPE html>
<html lang="en">
<head>
<meta charset="utf-8">
<title>Corvanta – Financial Services</title>
<link rel="stylesheet" href="https://fonts.googleapis.com/css2?family=Arimo:wght@400;700&family=Bebas+Neue&family=Open+Sans:wght@400;600&family=Noto+Serif:wght@700&display=swap">
<style>
:root{
  --navy:#0c4a8c;
  --blue:#1468b4;
  --blue-light:#2a8ad6;
  --sky:#27a6e0;
  --green:#4aa64a;
  --green-dark:#3b8f3b;
  --green-light:#66c15f;
  --text:#333;
  --muted:#555;
  --line:#d9d9d9;
  --panel:#f2f2f2;
  --link:#0d5aa7;
}
*{box-sizing:border-box;margin:0;padding:0}
html,body{width:1000px;height:1200px;overflow:hidden}
body{position:relative;font-family:"Arimo",Arial,sans-serif;color:var(--text);
  background:linear-gradient(to bottom,#0a3e80 0,#1a6fb8 20px,#0d4f97 80px,#0b4485 395px,#fff 395px,#fff 100%)}
.abs{position:absolute}
.page{left:120px;top:17px;width:756px;height:1172px;background:#fff;border-radius:14px;border:1px solid #e2e2e2}
.logo{left:147px;top:38px;display:flex;align-items:center;gap:12px}
.logo-mark{width:40px;height:40px;background:var(--blue)}
.logo-name{font-family:"Open Sans",sans-serif;font-size:50px;font-weight:400;color:var(--blue);letter-spacing:-1px;line-height:1}
.enquiry{left:780px;top:22px;width:90px;height:82px;background:var(--green-light);border-radius:14px 14px 0 14px;
  font-family:"Bebas Neue",sans-serif;color:#fff;font-size:22px;line-height:17px;padding:14px 0 0 13px}
.nav{left:125px;top:106px;width:746px;height:37px;background:linear-gradient(#1d7fd0,#0c5aa6);display:flex;border-radius:2px 2px 0 0}
.nav a{color:#fff;text-decoration:none;font-size:15px;line-height:37px;padding:0 10px;border-right:1px solid #3a8fd8;white-space:nowrap}
.nav a:last-child{border:0}
.nav .c{font-size:10px}
.hero{left:124px;top:143px;width:747px;height:252px;background:linear-gradient(100deg,#8e9297 0,#b8bbbf 25%,#d9dadc 45%,#eeeeee 65%,#f6f6f6 100%)}
.hero-title{left:548px;top:163px;font-family:"Bebas Neue",sans-serif;color:var(--blue);line-height:.9;text-align:right;width:317px}
.hero-title .l1{font-size:34px;color:#1b79c9}
.hero-title .l2{font-size:40px;color:var(--navy)}
.hero-band{left:140px;top:254px;width:731px;height:56px;background:rgba(255,255,255,.82);border-radius:28px 0 0 28px}
.hero-sub{font-family:"Bebas Neue",sans-serif;color:var(--green)}
.tabs{left:629px;top:362px;display:flex;gap:6px}
.tab{height:33px;padding:0 9px;font-size:15px;line-height:34px;color:#fff;border-radius:6px 6px 0 0}
.tab.on{background:var(--green);width:88px}
.tab.off{background:linear-gradient(#8b8b8b,#666);width:58px}
.login{left:629px;top:394px;width:232px;height:156px;background:var(--green);padding:10px 11px}
.login h4{font-size:10px;color:#fff;margin:0 0 9px 3px}
.field{height:32px;background:#fff;border-radius:5px;border:1px solid #dfe;font-size:12px;line-height:31px;padding-left:10px;margin-bottom:11px;color:#222}
.btn-login{display:inline-block;width:68px;height:27px;border:1px solid #bfe3b8;border-radius:4px;color:#fff;font-weight:700;font-size:13px;line-height:25px;text-align:center;background:var(--green-dark)}
.welcome{left:132px;top:406px;width:484px;font-size:9.5px;line-height:13.5px;color:var(--muted)}
.welcome h1{font-family:"Open Sans",sans-serif;font-weight:400;font-size:18px;color:#111;margin-bottom:8px}
.welcome h1 span{color:var(--blue)}
.welcome h5{font-size:9.5px;color:#111;margin:10px 0 6px}
.more{font-size:10px;font-weight:700;color:var(--link);text-align:right}
.services{left:124px;top:565px;width:747px;height:366px;background:linear-gradient(#5a5a5a 0,#6e6e6e 63px,#f3f3f3 63px)}
.services h2{font-family:"Open Sans",sans-serif;font-weight:400;font-size:17px;color:#fff;padding:5px 12px}
.card{top:596px;width:233px;height:320px;background:#fff;border:1px solid var(--line);border-radius:3px}
.card-head{height:33px;background:linear-gradient(var(--green-light),var(--green));color:#fff;font-family:"Open Sans",sans-serif;font-size:15px;line-height:33px;padding-left:8px;border-radius:3px 3px 0 0}
.card-img{margin:7px 7px 0;height:86px}
.card-body{padding:8px 7px 0;font-size:9px;line-height:13.6px;color:var(--muted)}
.card-body p+p{margin-top:8px}
.card-body h6{font-size:9px;color:#111;margin-bottom:7px}
.check-item{background:var(--panel);border:1px solid #e2e2e2;border-radius:3px;height:27px;margin:6px 4px 0;display:flex;align-items:center;gap:6px;padding-left:8px;font-size:9px;font-weight:700;color:#222}
.card-foot{position:absolute;bottom:0;left:0;right:0;height:25px;border-top:1px solid #eee;font-size:9.5px;font-weight:700;color:var(--link);text-align:right;padding:7px 9px 0}
.promise{left:134px;top:947px;width:480px;height:77px;border:1px solid var(--line);border-radius:3px;background:linear-gradient(#f2f2f2,#fff 43px)}
.promise h3{font-family:"Noto Serif",serif;font-size:14px;line-height:15px;color:var(--navy);padding:8px 0 0 12px}
.promise ul{list-style:none;display:flex;gap:0;border-top:1px solid var(--line);margin-top:9px;padding:10px 0 0 15px}
.promise li{display:flex;align-items:center;gap:5px;font-size:9.5px;font-weight:700;color:#222;width:158px}
.news{left:629px;top:947px;width:232px;height:77px;background:var(--green);border-radius:3px}
.news h3{font-family:"Open Sans",sans-serif;font-weight:600;font-size:14px;color:#fff;position:absolute;left:60px;top:9px}
.news-icon{position:absolute;left:14px;top:-6px}
.news-form{position:absolute;left:12px;top:38px;width:209px;height:28px;background:#fff;border-radius:3px;font-size:9.5px;line-height:28px;padding-left:8px}
.news-form b{position:absolute;right:1px;top:1px;width:69px;height:26px;background:linear-gradient(#1c6fc0,#0b4f98);color:#fff;font-size:12px;text-align:center;line-height:26px;border-radius:3px}
.footer{left:124px;top:1040px;width:747px;height:142px;background:linear-gradient(#0d5aa7,#1a78c6 60%,#0e5ca8);border-radius:0 0 4px 4px}
.fcol{position:absolute;top:8px;font-size:9.5px;color:#fff;line-height:16.5px}
.fcol h4{font-size:9.5px;margin-bottom:3px}
.fcol span::before{content:"▸ ";font-size:7px}
.fsep{position:absolute;top:0;width:1px;height:100px;background:#2e86d0}
.copy{position:absolute;left:0;right:0;top:112px;border-top:1px solid #3a8fd8;text-align:center;font-size:9px;color:#fff;padding-top:7px}
</style>
</head>
<body>
<div class="abs page"></div>

<header>
  <div class="abs logo"><span class="logo-mark"></span><span class="logo-name">Corvanta</span></div>
  <div class="abs enquiry">Send<br>an<br>enquiry ›</div>
</header>

<nav class="abs nav">
  <a style="width:67px">About <span class="c">⌄</span></a>
  <a style="width:164px">Accounting &amp; Advisory <span class="c">⌄</span></a>
  <a style="width:144px">Audit &amp; Assurance <span class="c">⌄</span></a>
  <a style="width:122px">Corvanta Super <span class="c">⌄</span></a>
  <a style="width:73px;text-align:center">Careers</a>
  <a style="width:102px;text-align:center">Newsletters</a>
  <a style="width:74px;text-align:center">Contact</a>
</nav>

<section>
  <div class="abs hero" role="img" aria-label="Photo of two business advisers reviewing documents at a table"></div>
  <div class="abs hero-title"><div class="l1">Corvanta is a multi-faceted</div><div class="l2">financial services firm</div></div>
  <div class="abs hero-band"></div>
  <div class="abs hero-sub" style="left:588px;top:257px;font-size:22px">Incorporating the skills of</div>
  <div class="abs hero-sub" style="left:165px;top:279px;font-size:28px;white-space:nowrap">Accountants &nbsp;|&nbsp; Business Advisers &nbsp;|&nbsp; Auditors and SMSF Specialists</div>
</section>

<div class="abs tabs"><div class="tab on">Accounting</div><div class="tab off">Super</div></div>
<form class="abs login">
  <h4>Log in to Corvanta Accounting</h4>
  <div class="field">Email Address</div>
  <div class="field">Password</div>
  <span class="btn-login">Login</span>
</form>

<section class="abs welcome">
  <h1>Welcome to <span>Corvanta</span></h1>
  <p>Corvanta is a financial services firm that incorporates the skills of accountants, business advisers, auditors and SMSF administrators across three interconnected service divisions.</p>
  <h5>The word Corvanta:</h5>
  <p>The word Corvanta can be found in the dictionary; it's more literal meaning is the connecting together of things of a different nature, the synthesis of creative ideas. It means the application of lateral thinking with the end aim of solving practical problems.</p>
  <p class="more" style="margin-top:7px">Read more ›</p>
</section>

<section class="abs services"><h2>Our Services</h2></section>

<article class="abs card" style="left:133px">
  <div class="card-head">Accounting &amp; Advisory</div>
  <div class="card-img" role="img" aria-label="Photo of two smiling accountants" style="background:linear-gradient(90deg,#6f6a66,#b9b2ab 50%,#e9e7e4)"></div>
  <div class="card-body">
    <p>Our Accounting and Advisory team - AG Corvanta Chartered Accountants - provide traditional accounting services and professional corporate and business advice. Our services include:</p>
  </div>
  <div class="check-item"><svg width="11" height="9"><path d="M1 5l3 3 6-7" stroke="#4aa64a" stroke-width="2" fill="none"/></svg>Accounting and Taxation Services</div>
  <div class="check-item"><svg width="11" height="9"><path d="M1 5l3 3 6-7" stroke="#4aa64a" stroke-width="2" fill="none"/></svg>Corporate and Business Advice</div>
  <div class="check-item"><svg width="11" height="9"><path d="M1 5l3 3 6-7" stroke="#4aa64a" stroke-width="2" fill="none"/></svg>Family Wealth Management</div>
  <div class="card-foot">Read more ›</div>
</article>

<article class="abs card" style="left:381px">
  <div class="card-head">Audit &amp; Assurance</div>
  <div class="card-img" role="img" aria-label="Photo of an auditor in an office with colleagues" style="background:linear-gradient(90deg,#e9dcc0,#c9c3bb 50%,#3d4250 65%,#d6d6d9)"></div>
  <div class="card-body">
    <h6>A COMMITTMENT TO AUDIT SERVICES</h6>
    <p>While the number of firms providing audit services has decreased in recent years, Corvanta remain committed to audit as a core service. We have embraced the challenges created by increasingly onerous auditing standards and the ever constant threat of litigation. By increasing both our human and technical resources we remain positioned at the forefront of our profession.</p>
  </div>
  <div class="card-foot">Read more ›</div>
</article>

<article class="abs card" style="left:629px">
  <div class="card-head">Self Managed Super Funds</div>
  <div class="card-img" role="img" aria-label="Photo of a business team standing in a bright office" style="background:linear-gradient(90deg,#9db7d3,#3d4b63 40%,#e8e6e3 70%,#b7c6d8)"></div>
  <div class="card-body">
    <p>Corvanta Super is a specialist division formed in July 2009 to specifically service our rapidly growing SMSF client base, in response to the continual growth of the SMSF industry.</p>
    <p>Our aim is to provide advisors, trustees and other related parties with practical and reliable solutions to make SMSF's easy.</p>
    <p>Over the past ten years, SMSF's have enjoyed the highest growth rate in the superannuation industry. In fact,</p>
  </div>
  <div class="card-foot">Read more ›</div>
</article>

<section class="abs promise">
  <h3>We offer peace of mind regarding the cost and delivery of<br>our services with a committment to:</h3>
  <ul>
    <li style="width:141px"><svg width="11" height="9"><path d="M1 5l3 3 6-7" stroke="#4aa64a" stroke-width="2" fill="none"/></svg>Quoted Upfront Fees</li>
    <li style="width:180px"><svg width="11" height="9"><path d="M1 5l3 3 6-7" stroke="#4aa64a" stroke-width="2" fill="none"/></svg>Guaranteed Turnaround Times</li>
    <li><svg width="11" height="9"><path d="M1 5l3 3 6-7" stroke="#4aa64a" stroke-width="2" fill="none"/></svg>Integrated Service Plans</li>
  </ul>
</section>

<section class="abs news">
  <svg class="news-icon" width="42" height="40" viewBox="0 0 42 40"><rect x="2" y="6" width="34" height="30" rx="3" fill="#dfe6ee" stroke="#8aa" /><path d="M2 9l17 14 17-14" fill="none" stroke="#7a8a9a" stroke-width="1.5"/><path d="M24 34l14-22 3 2-14 22z" fill="#333"/></svg>
  <h3>Get Our Newsletter!</h3>
  <div class="news-form">Enter your email address<b>Sign Up</b></div>
</section>

<footer class="abs footer">
  <div class="fcol" style="left:12px"><h4>About</h4><span>Includes History</span><br><span>Values</span><br><span>Our People</span><br><span>community etc</span></div>
  <div class="fsep" style="left:90px"></div>
  <div class="fcol" style="left:102px"><h4>Accounting &amp; Advisory</h4><span>About</span><br><span>Services</span><br><span>Tax &amp; Accounting</span><br><span>Business Advisory</span></div>
  <div class="fcol" style="left:196px;top:27px"><span>Family Wealth Management</span><br><span>Client Sign In</span><br><span>Calculators</span></div>
  <div class="fsep" style="left:328px"></div>
  <div class="fcol" style="left:339px"><h4>Audit &amp; Assurance</h4><span>About</span><br><span>Services</span></div>
  <div class="fsep" style="left:431px"></div>
  <div class="fcol" style="left:444px"><h4>Corvanta Super</h4><span>About</span><br><span>Individuals</span><br><span>Services</span><br><span>Advisers</span></div>
  <div class="fcol" style="left:512px;top:27px"><span>Services</span><br><span>Portal Sign In</span><br><span>Calculators</span></div>
  <div class="fsep" style="left:586px"></div>
  <div class="fcol" style="left:599px"><h4>Other Link</h4><span>Home</span><br><span>Careers</span><br><span>Newsletters</span></div>
  <div class="fcol" style="left:664px;top:27px"><span>Contact</span><br><span>Your Privacy</span><br><span>Site by Brightfold</span></div>
  <div class="copy">Copyright © 2011 Corvanta Group. All Rights Reserved.</div>
</footer>
</body>
</html>
```